Coral Wirelink Business Card

Hi, We need business cards for our sales agents for our business.
Please have a look at the website www.coralwirelink.co and also the attached files for some design expectation and different type of content to be placed on the card.
e.g. Job designation could be - Agent, Zoning Agent or Director. When you submit mock up please submit with variations in the data. Please provide fresh designs and let me know if any questions. Thanks

Industry/Entity Type

Business

```html
<!DOCTYPE html>
<html lang="en">
<head>
<meta charset="utf-8">
<title>Coral Wirelink Business Cards</title>
<link href="https://fonts.googleapis.com/css2?family=Open+Sans:wght@400;700&family=Tinos:ital@1&display=swap" rel="stylesheet">
<style>
  :root {
    --navy: #1c2333;
    --bar-navy: #14207a;
    --bar-blue: #2f7fe0;
    --orange: #f47216;
    --blue: #2962c8;
    --border: #7a7a7a;
    --ink: #111;
    --paper: #fff;
    --shadow-grey: #9a9a9a;
  }
  html, body {
    margin: 0;
    width: 1200px;
    height: 913px;
    overflow: hidden;
    background: var(--paper);
  }
  .card {
    position: absolute;
    top: 104px;
    width: 426px;
    height: 724px;
    border: 1px solid var(--border);
    box-sizing: border-box;
    background: var(--paper);
    overflow: hidden;
    font-family: "Open Sans", Arial, sans-serif;
  }
  .card--single { left: 119px; }
  .card--triptych { left: 681px; }

  .photo {
    position: absolute;
    top: 0;
    height: 330px;
  }
  .photo--interior {
    background: linear-gradient(180deg, #eef0ee 0%, #d9d8d2 45%, #b9b6ab 75%, #8d8a80 100%);
  }
  .photo--house {
    background: linear-gradient(180deg, #5d6470 0%, #7b7f86 25%, #d9cfb5 50%, #c9c0a4 75%, #8fa07a 100%);
  }
  .card--single .photo { left: 0; width: 426px; }
  .photo--left { left: 0; width: 135px; }
  .photo--middle { left: 141px; width: 140px; }
  .photo--right { left: 288px; width: 138px; top: 22px; height: 308px; }

  .bands {
    position: absolute;
    left: 0;
    top: 0;
    width: 426px;
    height: 724px;
  }
  .bands .white { fill: var(--paper); }
  .bands .orange { fill: var(--orange); }
  .bands .blue { fill: var(--blue); }
  .bands .bar-shadow { fill: var(--shadow-grey); }

  .brand {
    position: absolute;
    top: 445px;
    left: 0;
    width: 426px;
    text-align: center;
    font-weight: 700;
    font-size: 34px;
    color: var(--navy);
    letter-spacing: -0.5px;
    line-height: 44px;
  }
  .brand-dot {
    display: inline-block;
    width: 12px;
    height: 12px;
    border-radius: 50%;
    background: var(--orange);
    margin-left: 8px;
    vertical-align: 4px;
  }
  .tagline {
    position: absolute;
    top: 494px;
    left: 0;
    width: 426px;
    text-align: center;
    font-family: "Tinos", "Times New Roman", serif;
    font-style: italic;
    font-size: 21px;
    color: var(--navy);
  }
  .name-bar {
    position: absolute;
    top: 531px;
    left: 97px;
    width: 232px;
    height: 32px;
    background: linear-gradient(90deg, var(--bar-navy) 0%, #1f3fb0 55%, var(--bar-blue) 100%);
    color: var(--paper);
    font-weight: 700;
    font-size: 17px;
    line-height: 32px;
    text-align: center;
  }
  .contact {
    position: absolute;
    top: 616px;
    left: 0;
    width: 426px;
    text-align: center;
    font-size: 17px;
    line-height: 23px;
    color: var(--ink);
  }
  .contact p { margin: 0; }
</style>
</head>
<body>

<section class="card card--single">
  <div class="photo photo--interior" role="img" aria-label="Photo of a bright modern living room with sofas and shelving"></div>
  <svg class="bands" viewBox="0 0 426 724" aria-hidden="true">
    <path class="white" d="M0,305 Q213,280 426,305 L426,724 L0,724 Z"/>
    <path class="orange" d="M0,318 Q213,292 426,318 L426,344 Q213,318 0,344 Z"/>
    <path class="blue" d="M0,358 Q213,334 426,358 L426,370 Q213,346 0,370 Z"/>
    <path class="bar-shadow" d="M104,563 L322,563 Q318,572 310,580 Q215,568 112,580 Q106,572 104,563 Z"/>
  </svg>
  <div class="brand">CORAL WIRELINK<span class="brand-dot"></span></div>
  <div class="tagline">Linking Every Island</div>
  <div class="name-bar">REWA MANASE / AGENT</div>
  <div class="contact">
    <p>License Number:00000000</p>
    <p>Mobile: 0000000000</p>
    <p>Email: www.coralwirelink.co</p>
  </div>
</section>

<section class="card card--triptych">
  <div class="photo photo--interior photo--left" role="img" aria-label="Photo of a modern living room interior"></div>
  <div class="photo photo--house photo--middle" role="img" aria-label="Photo of a house exterior with gabled roof"></div>
  <div class="photo photo--interior photo--right" role="img" aria-label="Photo of a modern living room interior"></div>
  <svg class="bands" viewBox="0 0 426 724" aria-hidden="true">
    <path class="white" d="M0,305 Q213,280 426,305 L426,724 L0,724 Z"/>
    <path class="orange" d="M0,318 Q213,292 426,318 L426,344 Q213,318 0,344 Z"/>
    <path class="blue" d="M0,358 Q213,334 426,358 L426,370 Q213,346 0,370 Z"/>
    <path class="bar-shadow" d="M104,563 L322,563 Q318,572 310,580 Q215,568 112,580 Q106,572 104,563 Z"/>
  </svg>
  <div class="brand">CORAL WIRELINK<span class="brand-dot"></span></div>
  <div class="tagline">Linking Every Island</div>
  <div class="name-bar">REWA MANASE / AGENT</div>
  <div class="contact">
    <p>License Number:00000000</p>
    <p>Mobile: 0000000000</p>
    <p>Email: www.coralwirelink.co</p>
  </div>
</section>

</body>
</html>
```